Velmo Corporate Website for technological company

We need a modern website to promote our product and services.
You can found the actually website at the address: www.velmo-example.ch

We are a new company for B2B market. We would like do show our high precision and innovation capability.

we need a section were is possible to easily upload "news" and documents for our customers.

Target Market(s)

B2B services in the industry market

Industry/Entity Type

It Company

Coding

Coded - Design and coding required

Number of Pages Required

5+ page

Font styles to use
Other font styles liked:
• We accept propositions

Requirements
Must have
• Easy to maintain
• Presentation of the Velmo company
• Presentation of Velmo services and products
• The customer can download our ducumentation
Nice to have
• Sexy and modern

```html
<!DOCTYPE html>
<html lang="en">
<head>
<meta charset="utf-8">
<title>Velmo Control Systems</title>
<link rel="stylesheet" href="https://fonts.googleapis.com/css2?family=Open+Sans:wght@400;600;700&family=Play:wght@400;700&display=swap">
<style>
:root{
  --gold:#a89d5c;
  --gold-dark:#958a4c;
  --ink:#333333;
  --text:#555555;
  --dark:#2f2f2f;
  --darker:#262626;
  --panel:#f2f2f2;
  --line:#dddddd;
  --white:#ffffff;
}
*{box-sizing:border-box;margin:0;padding:0}
html,body{width:1200px;height:2483px;overflow:hidden}
body{position:relative;background:var(--white);font-family:'Open Sans',sans-serif;color:var(--text)}
.abs{position:absolute}
.heading{font-family:'Play',sans-serif;font-weight:700;color:var(--ink);text-transform:uppercase}
.btn{position:absolute;display:flex;align-items:center;justify-content:center;background:var(--gold);color:var(--white);font-family:'Play',sans-serif;font-weight:700;font-size:15px;letter-spacing:.5px;text-transform:uppercase}

/* header */
.top-strip{left:0;top:0;width:1200px;height:7px;background:var(--dark)}
.utility-tab{left:678px;top:0;width:444px;height:43px;background:var(--dark);clip-path:polygon(0 0,100% 0,97% 100%,3% 100%);display:flex;align-items:center;justify-content:center;gap:26px;color:#ddd;font-size:12.5px;font-family:'Play',sans-serif;text-transform:uppercase}
.utility-tab .phone{color:var(--gold)}
.utility-tab span{display:flex;align-items:center;gap:7px}
.brand{left:74px;top:52px;display:flex;align-items:center;gap:12px}
.brand-mark{width:48px;height:48px;background:var(--gold)}
.brand-name{font-family:'Play',sans-serif;font-weight:700;font-size:50px;color:#222;letter-spacing:1px}
.brand-suffix{font-family:'Play',sans-serif;font-weight:700;font-size:50px;color:#222}
.nav{top:84px;left:482px;display:flex;height:35px;align-items:center;font-family:'Play',sans-serif;font-weight:700;font-size:15px;color:#222;text-transform:uppercase}
.nav a{position:absolute;white-space:nowrap;text-decoration:none;color:inherit;line-height:35px}
.nav .active{background:var(--gold);color:var(--white);padding:0 14px}

/* hero */
.hero{left:0;top:129px;width:1200px;height:470px;background:radial-gradient(ellipse at 55% 45%,#d6d5d2 0%,#b9b8b5 55%,#8f8e8b 100%)}
.hero-title{left:0;top:283px;width:1200px;text-align:center;font-family:'Play',sans-serif;font-weight:700;font-size:57px;color:var(--white)}
.hero-sub{left:140px;top:366px;width:920px;text-align:center;font-size:17.5px;line-height:32px;color:var(--white)}
.hero-btn{left:498px;top:453px;width:204px;height:44px}
.dots{left:566px;top:557px;display:flex;gap:8px}
.dots i{display:block;width:12px;height:12px;border-radius:50%;background:#111}
.dots i:first-child{background:var(--white)}

/* welcome */
.welcome{left:74px;top:648px;width:682px}
.welcome h1{font-size:26px;margin-bottom:20px}
.welcome p{font-size:15.5px;line-height:25px;margin-bottom:12px}
.welcome .lead{color:var(--gold);font-weight:700;margin-top:18px;margin-bottom:10px}
.areas{list-style:none}
.areas li{display:flex;align-items:center;gap:12px;font-size:15.5px;line-height:32px}
.read-more{left:74px;top:1104px;width:152px;height:44px}
.brochure{left:794px;top:652px;width:331px;height:66px;background:var(--dark);display:flex;align-items:center;gap:24px;padding-left:26px;color:var(--white);font-family:'Play',sans-serif;font-weight:700;font-size:20px;line-height:23px;text-transform:uppercase}
.brochure small{font-size:13px}
.news{left:794px;top:736px;width:331px;height:409px;background:var(--panel);padding:22px 26px}
.news h2{font-size:26px;margin-bottom:18px}
.news-date{color:var(--gold);font-family:'Play',sans-serif;font-weight:700;font-size:14px;margin-bottom:10px}
.news p{font-size:15px;line-height:25px;color:#444}
.news hr{border:0;border-top:1px solid var(--line);margin:14px 0 16px}
.news-btn{left:821px;top:1076px;width:152px;height:45px}

/* services */
.services{left:0;top:1193px;width:1200px;height:488px;background:var(--dark)}
.services h2{position:absolute;top:48px;width:1200px;text-align:center;color:var(--white);font-size:26px}
.service{position:absolute;top:114px;width:270px;text-align:center}
.service svg{display:block;margin:0 auto;height:72px}
.service h3{font-family:'Play',sans-serif;font-weight:700;color:var(--gold);font-size:19px;margin-top:24px;margin-bottom:6px;text-transform:uppercase}
.service p{color:#ddd;font-size:14.5px;line-height:23px;padding:0 4px}
.services-btn{left:498px;top:1584px;width:204px;height:44px}

/* products */
.products-title{left:74px;top:1718px;font-size:26px}
.tab{position:absolute;left:74px;width:180px;height:46px;display:flex;align-items:center;padding-left:30px;font-family:'Play',sans-serif;font-weight:700;font-size:13.5px;text-transform:uppercase}
.tab-motor{top:1778px;background:var(--white);border:1px solid var(--line);border-right:0;color:#333;z-index:2}
.tab-bus{top:1831px;background:var(--gold);color:var(--white)}
.product-panel{left:253px;top:1778px;width:872px;height:327px;background:var(--panel);border:1px solid var(--line)}
.product-mark{left:278px;top:1812px;width:136px;height:50px;background:linear-gradient(90deg,#3a3a3a,#1a1a1a)}
.product-name{left:430px;top:1806px;font-family:'Play',sans-serif;font-weight:700;color:var(--gold);font-size:24px}
.product-tag{left:430px;top:1838px;font-family:'Play',sans-serif;font-weight:700;color:#222;font-size:13.5px;text-transform:uppercase}
.product-desc{left:278px;top:1874px;width:486px;font-size:15.5px;line-height:26px;color:#444}
.product-btn{left:278px;top:2024px;width:196px;height:45px}
.product-photo{left:793px;top:1812px;width:310px;height:258px;background:radial-gradient(circle at 50% 50%,#5e8f6a 0%,#3f6b4c 45%,#e8ece8 75%,#ffffff 100%);border:1px solid var(--line)}

/* footer */
.footer{left:0;top:2148px;width:1200px;height:335px;background:var(--dark);color:var(--white)}
.footer-brand{left:45px;top:2262px;display:flex;align-items:center;gap:14px}
.footer-brand .brand-mark{width:52px;height:52px}
.footer-brand .brand-name{color:var(--white);font-size:52px}
.footer-brand .brand-suffix{color:var(--white);font-size:52px}
.f-head{position:absolute;top:2188px;font-family:'Play',sans-serif;font-weight:700;font-size:19px;text-transform:uppercase;color:var(--white)}
.contact-list{left:400px;top:2240px;list-style:none;font-size:12.5px}
.contact-list li{display:flex;gap:14px;align-items:flex-start;line-height:20px;margin-bottom:13px}
.contact-list svg{flex:none;margin-top:3px}
.contact-list a{color:var(--white)}
.newsletter-text{left:636px;top:2234px;width:240px;font-size:13px;line-height:21px}
.email-field{left:637px;top:2295px;width:224px;height:35px;background:var(--white);color:#888;font-size:13px;display:flex;align-items:center;padding-left:14px}
.subscribe{left:637px;top:2340px;width:86px;height:28px;font-size:11px;font-family:'Open Sans',sans-serif;font-weight:600}
.follow-text{left:904px;top:2240px;width:250px;font-size:12px;line-height:20px}
.socials{left:904px;top:2321px;display:flex;gap:10px}
.socials i{display:block;width:36px;height:36px;border:2px solid var(--white);border-radius:50%}
.footer-rule{left:0;top:2408px;width:1200px;height:1px;background:#3d3d3d}
.copyright{left:0;top:2437px;width:1200px;text-align:center;font-size:12.5px;color:var(--white)}
</style>
</head>
<body>

<header>
  <div class="abs top-strip"></div>
  <div class="abs utility-tab">
    <span class="phone"><svg width="12" height="12" viewBox="0 0 24 24"><path fill="currentColor" d="M6.6 10.8a15.5 15.5 0 0 0 6.6 6.6l2.2-2.2c.3-.3.7-.4 1-.2 1.1.4 2.3.6 3.6.6.6 0 1 .4 1 1V20c0 .6-.4 1-1 1A17 17 0 0 1 3 4c0-.6.4-1 1-1h3.5c.6 0 1 .4 1 1 0 1.3.2 2.5.6 3.6.1.3 0 .7-.2 1z"/></svg>+41 (0)21 555 01 20</span>
    <span><svg width="11" height="12" viewBox="0 0 24 24"><circle cx="12" cy="7" r="5" fill="currentColor"/><path fill="currentColor" d="M2 23c0-6 4.5-9 10-9s10 3 10 9z"/></svg>Member log in</span>
    <span><svg width="22" height="14" viewBox="0 0 22 14"><rect width="22" height="14" fill="#3b4f8c"/><rect y="5" width="22" height="4" fill="#fff"/><rect x="9" width="4" height="14" fill="#fff"/><rect y="6" width="22" height="2" fill="#c8343a"/><rect x="10" width="2" height="14" fill="#c8343a"/></svg>EN <svg width="9" height="6" viewBox="0 0 9 6"><path d="M0 0h9L4.5 6z" fill="#ddd"/></svg></span>
  </div>
  <div class="abs brand"><span class="brand-mark"></span><span class="brand-name">VELMO</span><span class="brand-suffix" style="font-size:22px;margin-top:16px">Sagl</span></div>
  <nav class="abs nav" style="left:0">
    <a class="active" style="left:482px">Home</a>
    <a style="left:581px">Services</a>
    <a style="left:692px">Products</a>
    <a style="left:811px">Examples</a>
    <a style="left:927px">Download</a>
    <a style="left:1051px">Contacts</a>
  </nav>
</header>

<section>
  <div class="abs hero" role="img" aria-label="Photograph of an electronic control board connected by a ribbon cable and a USB lead"></div>
  <h1 class="abs hero-title">VELMO CONTROL SYSTEMS</h1>
  <p class="abs hero-sub">VELMO Ltd. designs systems in which electronics, software and mechanics are perfectly integrated to achieve uncompromising performance.</p>
  <a class="btn hero-btn">View products</a>
  <div class="abs dots"><i></i><i></i><i></i><i></i></div>
</section>

<section>
  <div class="abs welcome">
    <h1 class="heading">Welcome to our website</h1>
    <p>The ever-increasing complexity in modern systems, the search for reliability and performance and the continuous desire to reduce production costs and dimensions of the products require a rigorous integration between the electronic units, software and mechanical systems.</p>
    <p>VELMO Ltd. designs systems in which electronics, software and mechanics are perfectly integrated to achieve uncompromising performance.</p>
    <p>VELMO Ltd. designs systems in which electronics, software and mechanics are perfectly integrated to achieve uncompromising performance.</p>
    <p class="lead">VELMO Ltd. is a company active in the following areas:</p>
    <ul class="areas">
      <li><svg width="13" height="13" viewBox="0 0 16 16"><circle cx="8" cy="8" r="8" fill="var(--gold)"/><path d="M4.5 8.2l2.3 2.3 4.7-4.8" stroke="#fff" stroke-width="2" fill="none"/></svg>Simulation and modeling of complete processes</li>
      <li><svg width="13" height="13" viewBox="0 0 16 16"><circle cx="8" cy="8" r="8" fill="var(--gold)"/><path d="M4.5 8.2l2.3 2.3 4.7-4.8" stroke="#fff" stroke-width="2" fill="none"/></svg>Concept and design of electronic circuits and mechanical units</li>
      <li><svg width="13" height="13" viewBox="0 0 16 16"><circle cx="8" cy="8" r="8" fill="var(--gold)"/><path d="M4.5 8.2l2.3 2.3 4.7-4.8" stroke="#fff" stroke-width="2" fill="none"/></svg>Development of application specific control software</li>
      <li><svg width="13" height="13" viewBox="0 0 16 16"><circle cx="8" cy="8" r="8" fill="var(--gold)"/><path d="M4.5 8.2l2.3 2.3 4.7-4.8" stroke="#fff" stroke-width="2" fill="none"/></svg>Rapid prototyping (electronic cards, mechanisms ...)</li>
    </ul>
  </div>
  <a class="btn read-more">Read more</a>

  <a class="abs brochure">
    <svg width="34" height="32" viewBox="0 0 34 32"><path d="M13 0h8v12h6l-10 10L7 12h6z" fill="var(--gold)"/><path d="M2 20v10h30V20" stroke="var(--gold)" stroke-width="4" fill="none"/></svg>
    <span>Downlaod<br>brochure Velmo <small>(EN)</small></span>
  </a>
  <aside class="abs news">
    <h2 class="heading">Latest news</h2>
    <div class="news-date">OCT 16, 2016</div>
    <p>The Velmo team will be present at the stand A16 of Techmex exhibition in Bern, between 6 and 8 september 2016.</p>
    <hr>
    <div class="news-date">OCT 16, 2016</div>
    <p>Added the 'application' page, showing some of the developments of Velmo Ltd...</p>
  </aside>
  <a class="btn news-btn">Read all news</a>
</section>

<section class="abs services">
  <h2 class="heading">Our services</h2>
  <div class="service" style="left:60px">
    <svg viewBox="0 0 72 72" width="72"><rect x="14" y="14" width="44" height="44" rx="4" fill="none" stroke="#fff" stroke-width="5"/><rect x="24" y="24" width="24" height="24" fill="#fff"/><g stroke="#fff" stroke-width="4"><path d="M24 2v10M36 2v10M48 2v10M24 60v10M36 60v10M48 60v10M2 24h10M2 36h10M2 48h10M60 24h10M60 36h10M60 48h10"/></g></svg>
    <h3>Electronics</h3>
    <p>VELMO Sàrl being active in all fields associated with actuator electronics, can develop solutions integrating...</p>
  </div>
  <div class="service" style="left:330px">
    <svg viewBox="0 0 72 72" width="72"><path fill="#fff" d="M31 6h10l2 8 6 3 7-4 7 7-4 7 3 6 8 2v10l-8 2-3 6 4 7-7 7-7-4-6 3-2 8H31l-2-8-6-3-7 4-7-7 4-7-3-6-8-2V31l8-2 3-6-4-7 7-7 7 4 6-3z"/><circle cx="36" cy="36" r="9" fill="var(--dark)"/></svg>
    <h3>Mechanics</h3>
    <p>VELMO Sàrl being active in all fields associated with actuator electronics, can develop solutions integrating...</p>
  </div>
  <div class="service" style="left:600px">
    <svg viewBox="0 0 72 72" width="72"><rect x="12" y="12" width="48" height="34" rx="3" fill="none" stroke="#fff" stroke-width="4"/><path d="M4 52h64l-4 8H8z" fill="#fff"/></svg>
    <h3>Software</h3>
    <p>VELMO Sàrl being active in all fields associated with actuator electronics, can develop solutions integrating...</p>
  </div>
  <div class="service" style="left:870px">
    <svg viewBox="0 0 110 72" width="110"><rect x="12" y="4" width="86" height="56" rx="3" fill="none" stroke="#fff" stroke-width="4"/><path d="M2 64h106v4H2z" fill="#fff"/><path d="M42 22l13-6 13 6v15l-13 6-13-6z M42 22l13 6 13-6 M55 28v15" fill="none" stroke="#fff" stroke-width="3"/></svg>
    <h3>Simulation &amp; modeling</h3>
    <p>VELMO Sàrl being active in all fields associated with actuator electronics, can develop solutions integrating...</p>
  </div>
</section>
<a class="btn services-btn">View all services</a>

<section>
  <h2 class="abs heading products-title">Our products</h2>
  <div class="abs product-panel"></div>
  <div class="tab tab-motor">Motor driver</div>
  <div class="tab tab-bus">Bus interface</div>
  <div class="abs product-mark" role="img" aria-label="Product emblem illustration of a bird in flight"></div>
  <div class="abs product-name">SKYLARK:</div>
  <div class="abs product-tag">Intelligent control for electric motors</div>
  <p class="abs product-desc">Skylark is an electronics board developed for the control of DC and BLDC motors with a power ranging from 1W to 250W. This board integrates a powerful 32-bit processor, a power stage, two communication buses, a number of interfaces compatible with the different position sensor standards available on the market...</p>
  <a class="btn product-btn">View all product</a>
  <div class="abs product-photo" role="img" aria-label="Photograph of the motor control circuit board with green terminal connectors"></div>
</section>

<footer>
  <div class="abs footer"></div>
  <div class="abs footer-brand"><span class="brand-mark"></span><span class="brand-name">VELMO</span><span class="brand-suffix" style="font-size:22px;margin-top:18px">Sàrl</span></div>

  <div class="f-head" style="left:400px">Contact us</div>
  <ul class="abs contact-list">
    <li><svg width="14" height="12" viewBox="0 0 24 20"><path fill="#fff" d="M2 2c6-3 14-3 20 0v5h-6V5H8v2H2z"/><rect x="3" y="9" width="18" height="11" rx="2" fill="#fff"/></svg>+41 (0)21 555 01 20 (Phone)</li>
    <li><svg width="14" height="13" viewBox="0 0 24 22"><rect x="6" y="0" width="12" height="7" fill="#fff"/><rect x="0" y="7" width="24" height="10" rx="2" fill="#fff"/><rect x="6" y="14" width="12" height="8" fill="#fff" stroke="var(--dark)" stroke-width="2"/></svg>+41 (0)21 555 01 21 (Fax)</li>
    <li><svg width="14" height="11" viewBox="0 0 24 18"><rect width="24" height="18" fill="#fff"/><path d="M0 0l12 10L24 0" stroke="var(--dark)" stroke-width="2" fill="none"/></svg><a>info@velmo-example.ch (Email)</a></li>
    <li><svg width="12" height="16" viewBox="0 0 16 22"><path fill="#fff" d="M8 0a8 8 0 0 1 8 8c0 6-8 14-8 14S0 14 0 8a8 8 0 0 1 8-8z"/><circle cx="8" cy="8" r="3" fill="var(--dark)"/></svg><span>Chemin des Vergers 8<br>CH - 1700 Fribourg</span></li>
  </ul>

  <div class="f-head" style="left:636px">Newsletter</div>
  <p class="abs newsletter-text">Register Your email address to get information about us</p>
  <div class="abs email-field">Email Address</div>
  <a class="btn subscribe">SUBSCRIBE</a>

  <div class="f-head" style="left:904px">Follow us</div>
  <p class="abs follow-text">Lorem ipsum dolor sit amet, conse ctetur adipiscing elit. Nulla in purus nibh. Donec ornare</p>
  <div class="abs socials"><i></i><i></i><i></i><i></i><i></i></div>

  <div class="abs footer-rule"></div>
  <p class="abs copyright">Copyright © velmo. All rights reserved</p>
</footer>

</body>
</html>
```